Sticker label design for - Tidal Fern Deodorant Balm

I need a label for my 100% Natural Deodorant Balm
The brand is called "Plum Meadow Brand", and the product is called TIDAL FERN Deodorant Balm.
There are two labels, one is a 5.2cm circle for the top, and 4.5cm circle for the base. The jar is amber plastic with black lid.
Width: 5.8cm
Height: 3.4cm (Lid 1.2cm, base 2,2cm)
Here is a link to what the jar looks like from one of my competitors: https://copperwren.com.au/products/body/velaro-deodorant-paste/
The product is a unisex product. Please see uploaded files for designs previously made for the brand. I'm trying to see a few more designs before finalising my choice. Feel free to use the logo at the top (Plum Meadow Brand) of either attachment if you would like. Or design your own.
Be be aware that it is meant to be Aluminium and Paraben Free, not "Parabens" Weight of product is 70g, please include this.
Label can be any colour, and printed with regular colours or event gold, silver or rose gold foil. Would a background be nice?
This is something I saw that I liked:
http://www.mossvelbalm.com
However I'm really open to what people can come up with.
For the back base-
Tidal Fern deodorant balm is made from 100% natural ingredients, and works by neutralises odour and minimising wetness without the use of harmful chemicals.
www.plummeadowbrand.com
Directions: For optimal result, apply a pea size amount of the balm to your dry armpits. Gently rub the balm into your armpits covering the entire area. Discontinue use if irritation occurs.
Ingredients: Shea Butter, Coconut oil, Sodium Bicarbonate, Arrowroot, Kaolin Clay, Vitamin E, Vegetable Glycerin, Activated Charcoal, Essential oils of Peppermint, Lavender, Mandarin, Tea tree, Geranium Rose & Cedarwood.
MADE IN AUSTRALIA
Reason: Hi,
I'm not getting many submissions, so was hoping to extend the deadline.
Skin Care Product

```html
<!DOCTYPE html>
<html lang="en">
<head>
<meta charset="utf-8">
<title>Tidal Fern Deodorant Balm – Lid Label</title>
<link rel="stylesheet" href="https://fonts.googleapis.com/css2?family=Oswald:wght@500&family=Open+Sans:wght@600&family=Sriracha&display=swap">
<style>
  :root {
    --page: #ffffff;
    --label-black: #1b1819;
    --label-rim: #0e0c0d;
    --blush: #e6a9b9;
    --blush-band: #e2b0bf;
    --ink-dark: #2b2326;
    --white: #ffffff;
  }
  * { margin: 0; padding: 0; box-sizing: border-box; }
  html, body {
    width: 1200px;
    height: 1200px;
    overflow: hidden;
    background: var(--page);
  }
  .canvas {
    position: relative;
    width: 1200px;
    height: 1200px;
  }
  .lid-label {
    position: absolute;
    left: 100px;
    top: 100px;
    width: 1000px;
    height: 1000px;
    border-radius: 50%;
    background: var(--label-black);
    border: 14px solid var(--label-rim);
  }
  .lid-label > * {
    position: absolute;
    left: 0;
    width: 100%;
    text-align: center;
  }
  .brand-name {
    top: 200px;
    font-family: "Open Sans", sans-serif;
    font-weight: 600;
    color: var(--blush);
    line-height: 1;
  }
  .brand-name .brand-main {
    display: block;
    font-size: 62px;
    letter-spacing: 2px;
  }
  .brand-name .brand-sub {
    display: block;
    margin-top: 14px;
    font-size: 30px;
    letter-spacing: 10px;
  }
  .product-name {
    top: 345px;
    font-family: "Oswald", sans-serif;
    font-weight: 500;
    font-size: 148px;
    line-height: 1;
    color: var(--blush);
    letter-spacing: 1px;
  }
  .product-band {
    top: 480px;
    left: 213px;
    width: 530px;
    height: 66px;
    background: var(--blush-band);
    font-family: "Sriracha", cursive;
    font-size: 50px;
    line-height: 66px;
    color: var(--ink-dark);
    letter-spacing: 1px;
  }
  .flourish {
    top: 562px;
    left: 447px;
    width: 92px;
    height: 18px;
    border-radius: 9px;
    background: linear-gradient(90deg, rgba(255,255,255,0.15), rgba(255,255,255,0.55), rgba(255,255,255,0.15));
  }
  .natural-claim {
    top: 592px;
    font-family: "Open Sans", sans-serif;
    font-weight: 600;
    font-size: 42px;
    color: var(--white);
    display: flex;
    justify-content: center;
    align-items: center;
    gap: 14px;
  }
  .leaf-mark {
    display: inline-block;
    width: 30px;
    height: 16px;
    border-radius: 50%;
    background: var(--white);
  }
  .free-from {
    top: 652px;
    font-family: "Open Sans", sans-serif;
    font-weight: 600;
    font-size: 40px;
    line-height: 48px;
    color: var(--white);
  }
  .net-weight {
    top: 772px;
    font-family: "Open Sans", sans-serif;
    font-weight: 600;
    font-size: 38px;
    color: var(--white);
  }
</style>
</head>
<body>
  <main class="canvas">
    <section class="lid-label">
      <div class="brand-name">
        <span class="brand-main">PLUM MEADOW</span>
        <span class="brand-sub">BRAND</span>
      </div>
      <h1 class="product-name">TIDAL FERN</h1>
      <div class="product-band">Deodorant Balm</div>
      <div class="flourish" role="img" aria-label="Small decorative swirl flourish"></div>
      <p class="natural-claim">
        <span class="leaf-mark" role="img" aria-label="Leaf ornament"></span>
        100% Natural
        <span class="leaf-mark" role="img" aria-label="Leaf ornament"></span>
      </p>
      <p class="free-from">Aluminium &amp; Paraben Free,<br>not Parabens</p>
      <p class="net-weight">70g</p>
    </section>
  </main>
</body>
</html>
```